Locksmith Business Cards

My father-in-law is in need of new business cards for his locksmith business and I need to impress him. Kindly help me out!

You can see the previous business card attached. It is a family run business in North Wales.

No individual names on the cards.

Key Things to Feature:
- The words "Prompt", "Local", "Reliable" (as you can see under the logo on the website)
- 24h Emergency Service
- Covering All of North Wales, the Wirral and Chester
- The color blue
- A key or a lock would be interesting (similar to the ones that come up when you google locksmith business card)

Optional (only if design includes bullet points, like the example below):
https://imgvaultcdnx.net/design_img/318264/57190/57190_2749031_318264_image.jpg
- Residential / Commercial / Automotive
- Alarms & Cameras
- Key Cutting & Safes

https://www.bryncoed-locksmiths-demo.co.uk/

Locksmith

01632 960 418
07700 900 362
bryncoedlocksmiths@mailvalex.com
Bryncoed Locksmiths, Hafod Barn, 4 Pennant Rd., Llandudno LL39 7QZ
www.bryncoed-locksmiths-demo.co.uk

• - The words "Prompt", "Local", "Reliable" (as you can see under the logo on the website)
• - 24h Emergency Service
• - Covering All of North Wales, the Wirral and Chester
• - A key or a lock would be interesting (similar to the ones that come up when you google locksmith business card)

```html
<!DOCTYPE html>
<html lang="en">
<head>
<meta charset="utf-8">
<title>Bryncoed Locksmiths – Business Card</title>
<link href="https://fonts.googleapis.com/css2?family=Open+Sans:wght@400&display=swap" rel="stylesheet">
<style>
  :root {
    --ink-black: #0b0b0c;
    --ink-dark: #1c1d20;
    --text-light: #e9e9ea;
    --brand-blue: #3a95f0;
    --row-1: #3b86de;
    --row-2: #3079d2;
    --row-3: #2e73c9;
    --row-4: #2a5ea6;
    --edge-blue: #4490ea;
    --icon-strip: #2b2c2f;
    --icon-strip-low: #222a38;
  }
  * { margin: 0; padding: 0; box-sizing: border-box; }
  html, body { width: 1200px; height: 706px; overflow: hidden; background: var(--ink-black); }
  body { font-family: "Open Sans", Arial, sans-serif; }

  .card { position: relative; width: 1200px; height: 706px; overflow: hidden; background: var(--ink-black); }

  .backdrop {
    position: absolute; left: 0; top: 0; width: 1200px; height: 706px;
    background: radial-gradient(ellipse at 30% 40%, #2a2b2e 0%, #141416 45%, var(--ink-black) 80%);
  }

  .brand { position: absolute; left: 116px; top: 240px; width: 470px; }
  .brand-row { display: flex; align-items: center; gap: 16px; }
  .brand-mark { width: 52px; height: 52px; background: var(--brand-blue); flex: none; }
  .brand-name {
    color: var(--text-light); font-size: 38px; line-height: 42px; font-weight: 400;
    letter-spacing: 1px; text-transform: uppercase;
  }
  .tagline {
    position: absolute; left: 116px; top: 335px; width: 355px; text-align: center;
    color: var(--brand-blue); font-size: 26px; letter-spacing: 0.5px;
  }
  .coverage {
    position: absolute; left: 16px; top: 648px; color: var(--text-light);
    font-size: 19px; letter-spacing: 0.2px;
  }

  .contact-panel { position: absolute; left: 586px; top: 0; width: 540px; height: 706px; }
  .edge { position: absolute; left: 0; top: 0; width: 21px; height: 706px; background: var(--edge-blue); }
  .row { position: absolute; left: 21px; width: 519px; display: flex; align-items: center; }
  .row-hours { top: 0; height: 179px; background: var(--row-1); }
  .row-address { top: 179px; height: 174px; background: var(--row-2); }
  .row-phone { top: 353px; height: 182px; background: var(--row-3); }
  .row-web { top: 535px; height: 171px; background: var(--row-4); }

  .icon-cell {
    width: 78px; height: 100%; background: var(--icon-strip);
    display: flex; align-items: center; justify-content: center; flex: none;
  }
  .row-web .icon-cell { background: var(--icon-strip-low); }
  .icon { width: 58px; height: 58px; }
  .icon .stroke { fill: none; stroke: var(--brand-blue); stroke-width: 5; stroke-linecap: round; }
  .icon .fill { fill: var(--brand-blue); }

  .row-text {
    flex: 1; text-align: center; color: var(--text-light);
    text-transform: uppercase; padding-right: 6px;
  }
  .hours { font-size: 31px; line-height: 34px; letter-spacing: 1px; }
  .address { font-size: 23px; line-height: 26px; letter-spacing: 0.5px; }
  .phones { font-size: 31px; line-height: 34px; letter-spacing: 1px; }
  .web { font-size: 21px; line-height: 38px; letter-spacing: 0.5px; }
</style>
</head>
<body>
<main class="card">
  <div class="backdrop" role="img" aria-label="Dark background with a faint network of connected dots and lines"></div>

  <section class="brand">
    <div class="brand-row">
      <span class="brand-mark"></span>
      <h1 class="brand-name">Bryncoed<br>Locksmiths</h1>
    </div>
  </section>
  <p class="tagline">PROMPT•LOCAL•RELIABLE</p>
  <p class="coverage">COVERING ALL OF NORTH WALES, THE WIRRAL AND CHESTER</p>

  <section class="contact-panel">
    <div class="edge"></div>

    <div class="row row-hours">
      <div class="icon-cell">
        <svg class="icon" viewBox="0 0 60 60" aria-hidden="true">
          <rect class="fill" x="24" y="4" width="12" height="5" rx="1"/>
          <circle class="stroke" cx="30" cy="34" r="20"/>
          <line class="stroke" x1="30" y1="34" x2="30" y2="22"/>
          <line class="stroke" x1="47" y1="15" x2="51" y2="11"/>
        </svg>
      </div>
      <p class="row-text hours">24 Hours<br>Emergency Service</p>
    </div>

    <div class="row row-address">
      <div class="icon-cell">
        <svg class="icon" viewBox="0 0 60 60" aria-hidden="true">
          <path class="fill" d="M30 2C19 2 11 10 11 21c0 14 19 37 19 37s19-23 19-37C49 10 41 2 30 2zm0 27a8 8 0 1 1 0-16 8 8 0 0 1 0 16z"/>
        </svg>
      </div>
      <p class="row-text address">Bryncoed Locksmiths,<br>Hafod Barn, 4 Pennant<br>Rd., Llandudno LL39 7QZ</p>
    </div>

    <div class="row row-phone">
      <div class="icon-cell">
        <svg class="icon" viewBox="0 0 60 60" aria-hidden="true">
          <path class="fill" d="M14 6l9 11-5 6c3 7 9 13 16 16l6-5 11 9-6 9C24 50 6 32 5 12z"/>
          <path class="fill" d="M36 6h18v5H42v12h-6z"/>
        </svg>
      </div>
      <p class="row-text phones">01632 960 418<br>07700 900 362</p>
    </div>

    <div class="row row-web">
      <div class="icon-cell">
        <svg class="icon" viewBox="0 0 60 60" aria-hidden="true">
          <circle class="fill" cx="30" cy="30" r="26"/>
          <path d="M16 16c6 2 10 6 9 12-4 1-8 5-6 10l-4 2c-5-7-4-17 1-24zM34 10c7 1 12 6 14 13-4 0-6 4-9 3-2-4-7-3-6-9 2-2 3-4 1-7zM35 34c5 0 9 2 8 7-2 5-6 9-11 10 1-5-1-11 3-17z" fill="#1d3f72"/>
        </svg>
      </div>
      <p class="row-text web">bryncoedlocksmiths@mailvalex.com<br>www.bryncoed-locksmiths-demo.co.uk</p>
    </div>
  </section>
</main>
</body>
</html>
```